9x12 Business Brochure, 3 fold, for Internet Marketing Company

I'd like to have a brochure designed for my Internet marketing company. I have the content all ready, 10 Internet Marketing Myths, which you can see here: http://www.brightfieldwebgrowth.net/usual-online-promo-fables/. I'm looking for something creative and business to business. The company is all about Internet marketing. I like the "http://" header I use at our website. People like it too and identify with it. Audience is business owners 35 to 55 years old. I use blue at my website. I *think* I would like the cover page (front page) to open with some attention grabbing text, that basically takes most of the front page of the brochure. It would probably say: "I Can Help You Get BETTER RESULTS from Your Website, More Traffic, TOP RANKINGS at Zorvix, More Leads and MORE SALES. But first you'll have to avoid these common Internet marketing myths..." The inside pages would have the content from above (the 10 myths). The back page would have testimonials that I can provide. And the inside folded in page (or what I call the inside folded in page) would have a list of services. I think I want the dimensions 12x9 which is a larger sized, three-fold brochure.

Target Market(s)

I use this brochure to send to business owners and managers to show them I know what I'm talking about and and expert. See attachment for content.

Industry/Entity Type

Marketing

Requirements
Should not have
• No clipart. Probably not illustrations. Photos. The "http://" used at the site is something people "connect" with and get that this is about Internet marketing.

```html
<!DOCTYPE html>
<html lang="en">
<head>
<meta charset="utf-8">
<title>Dana Whitfield Consulting – Tri-fold Brochure</title>
<link href="https://fonts.googleapis.com/css2?family=Carlito:ital,wght@0,400;0,700;1,400;1,700&display=swap" rel="stylesheet">
<style>
  :root{
    --page:#ffffff;
    --navy:#2b2f8c;
    --navy-deep:#26285f;
    --navy-mid:#2d3190;
    --glow:#1a76c4;
    --sky:#4bb0e6;
    --sky-soft:#8fd3f5;
    --ink:#ffffff;
    --quote:#1c2368;
    --photo-dark:#1e2d55;
    --photo-light:#dfe9f5;
  }
  *{margin:0;padding:0;box-sizing:border-box}
  html,body{width:1200px;height:1000px;overflow:hidden;background:var(--page)}
  body{font-family:"Carlito",Calibri,sans-serif;color:var(--ink);position:relative}

  .brochure{position:absolute;left:36px;top:78px;width:1125px;height:844px;display:flex}
  .panel{position:relative;height:100%;overflow:hidden}
  .panel--services{width:364px;background:radial-gradient(ellipse at 60% 35%,#2c5fb0 0%,var(--navy) 65%)}
  .panel--stories{width:381px;background:radial-gradient(ellipse at 20% 45%,var(--glow) 0%,var(--navy-mid) 55%,var(--navy) 100%);border-left:1px solid #1b1d4a}
  .panel--cover{width:380px;background:radial-gradient(ellipse at 55% 60%,#1e8ad6 0%,#2358b0 45%,var(--navy) 90%);border-left:1px solid #1b1d4a}

  .panel__head{position:absolute;left:0;top:0;width:100%;height:75px;background:var(--navy-deep)}
  .panel__title{position:absolute;top:47px;font-size:27px;font-weight:700;color:var(--sky);letter-spacing:.2px}
  .panel--services .panel__title{left:25px}
  .panel--stories .panel__title{left:45px}

  .services-list{position:absolute;left:27px;top:106px;list-style:none;font-size:16px;line-height:24.7px}
  .services-list li::before{content:"•";margin-right:9px}

  .motto{position:absolute;left:26px;top:592px;font-size:21px;font-weight:700;font-style:italic;color:var(--quote);line-height:24px}
  .motto span{display:block;padding-left:12px}

  .photo{position:absolute;display:block}
  .photo--keys{left:0;bottom:0}
  .photo--address{left:0;top:525px}

  .stories{position:absolute;left:45px;top:116px;width:295px;font-size:13.6px;line-height:18.6px}
  .story{margin-bottom:18.6px;font-style:italic}
  .story b{font-style:normal;font-weight:700}

  .footer{position:absolute;left:0;bottom:0;width:100%;height:47px;background:var(--navy-deep);display:flex;justify-content:space-between;align-items:center;padding:0 22px 4px 16px;font-size:15px}

  .pitch{position:absolute;left:34px;top:63px;color:var(--sky-soft)}
  .pitch__line{font-size:25px;line-height:30px;color:#44aee6}
  .pitch__big{font-size:31px;font-weight:700;color:var(--ink);line-height:34px}
  .pitch__list{position:absolute;left:67px;top:210px}
  .pitch__list .pitch__big{font-size:33px;line-height:36px}
  .pitch__list .pitch__huge{font-size:47px;font-weight:700;line-height:50px;color:var(--ink)}
  .pitch__note{position:absolute;left:69px;top:431px;font-size:16.5px;font-style:italic;line-height:22px;color:#e6eefa}
</style>
</head>
<body>
<main class="brochure">

  <section class="panel panel--services">
    <div class="panel__head"></div>
    <h2 class="panel__title">Services &amp; Expertise</h2>
    <ul class="services-list">
      <li>Internet Strategy Development</li>
      <li>Custom Website Design</li>
      <li>Blog Design &amp; Support</li>
      <li>Online Marketing Copywriting</li>
      <li>Social Media Marketing</li>
      <li>Search Engine Optimization (SEO)</li>
      <li>Conversion Optimization</li>
      <li>Content Marketing Management</li>
      <li>Using Circlebook for Business</li>
      <li>Zorvix+, Vidstream, Pinboardly</li>
      <li>Email Marketing &amp; Production</li>
      <li>Inquiry and Lead Development</li>
      <li>Zorvix Promote Pay-Per-Click</li>
      <li>Zorvix Local Places (maps)</li>
      <li>E-Commerce Development</li>
      <li>High-Performance Hosting</li>
      <li>Security &amp; Contingency Planning</li>
      <li>One-on-One or Group Training</li>
    </ul>
    <svg class="photo photo--keys" width="364" height="190" viewBox="0 0 364 190" role="img" aria-label="Close-up photo of a computer keyboard in blue light">
      <defs>
        <linearGradient id="keysTone" x1="0" y1="1" x2="1" y2="0">
          <stop offset="0" stop-color="#0c1330"/>
          <stop offset=".6" stop-color="#3a4f78"/>
          <stop offset="1" stop-color="#8ea4c6"/>
        </linearGradient>
      </defs>
      <polygon points="0,62 364,0 364,190 0,190" fill="url(#keysTone)"/>
    </svg>
    <p class="motto">“ If you think it’s expensive to hire<span>an expert, wait until you</span><span>hire an amateur.”</span></p>
  </section>

  <section class="panel panel--stories">
    <div class="panel__head"></div>
    <h2 class="panel__title">Success Stories</h2>
    <div class="stories">
      <p class="story"><b>Zorvix Rankings</b> – “… we have spent over a year trying to get onto page one at Zorvix. I has been very frustrating and we’ve wasted a lot of time and money. Dana explained everything very clearly and we did everything he told us. 90 days later we’re now showing up on the first page of Zorvix!</p>
      <p class="story"><b>Website Design</b> – “We needed a new website that properly reflected our company and the products and services we sell. We started getting more leads within 72 hours of launching the new site Dana and his team designed for us. We’re also getting better results from our Zorvix Promote pay-per-click advertising and more of those clicks are turning into inquiries!”</p>
      <p class="story"><b>More to Come</b> - Lorem ipsum dolor sit amet, consectetur adipiscing elit. Suspendisse justo velit, auctor ut pulvinar a, egestas non urna. Suspendisse potenti. Sed at pellentesque dolor. Vivamus sed nibh nisl. Nunc tortor tellus, facilisis eget pretium vitae, porttitor quis libero.</p>
      <p class="story"><b>More to Come</b> - Lorem ipsum dolor sit amet, consectetur adipiscing elit. Suspendisse justo velit, auctor ut pulvinar a, egestas non urna. Suspendisse potenti. Sed at pellentesque dolor. Vivamus sed nibh nisl. Nunc tortor tellus, facilisis eget pretium vitae, porttitor quis libero.</p>
      <p class="story"><b>More to Come</b> - Lorem ipsum dolor sit amet, consectetur adipiscing elit. Suspendisse justo velit, auctor ut pulvinar a, egestas non urna. Suspendisse potenti. Sed at pellentesque dolor.</p>
    </div>
    <footer class="footer"><span>Dana Whitfield Consulting (.com)</span><span>(866) 555-0148</span></footer>
  </section>

  <section class="panel panel--cover">
    <div class="pitch">
      <div class="pitch__line">I Can Help You Get</div>
      <div class="pitch__big">BETTER RESULTS</div>
      <div class="pitch__line">from Your Website:</div>
    </div>
    <div class="pitch__list">
      <div class="pitch__line">More Traffic,</div>
      <div class="pitch__big">TOP RANKINGS</div>
      <div class="pitch__line">with Zorvix,</div>
      <div class="pitch__line">More Inquiries, and</div>
      <div class="pitch__huge">MORE SALES.</div>
    </div>
    <p class="pitch__note">But first you’ll need to avoid these<br>Common Internet Marketing Myths…</p>
    <svg class="photo photo--address" width="380" height="272" viewBox="0 0 380 272" role="img" aria-label="Photo of a browser address bar showing http://www with a mouse pointer">
      <defs>
        <linearGradient id="addressTone" x1="0" y1="0" x2="1" y2="1">
          <stop offset="0" stop-color="var(--photo-light)"/>
          <stop offset=".55" stop-color="#b9cce6"/>
          <stop offset="1" stop-color="#5e7fb4"/>
        </linearGradient>
      </defs>
      <polygon points="0,88 380,0 380,272 0,272" fill="url(#addressTone)"/>
    </svg>
    <footer class="footer"><span>Dana Whitfield Consulting (.com)</span><span>(866) 555-0148</span></footer>
  </section>

</main>
</body>
</html>
```